Stationery Design Project

I am looking to create stationary for our new airport valet company. I am looking for something modern and stylish.

i also want to have a faint picture of something in the background (like a hollogram) something related to valet.

Our company is called Harborline Valet & Concierge.

Project Deadline Extended
Reason: To Finalize the edits with the designer who has so far provided the total package of what we are looking for in stationary.

Target Market(s)

high end customers

Industry/Entity Type

Airport

Requirements
Must have
• 1. name of company
2. address
3. 705 555 0173 (to be provided)
4. Harborline should be Black and Valet and Concierge should white
5. picture of valet or something relating to valet as a watermark on letterhead.

```html
<!DOCTYPE html>
<html lang="en">
<head>
<meta charset="utf-8">
<title>Harborline Valet &amp; Concierge — Stationery</title>
<link rel="stylesheet" href="https://fonts.googleapis.com/css2?family=Cinzel:wght@400&family=Questrial&display=swap">
<style>
  :root{
    --bg:#e6e6e6;
    --paper:#f7f7f7;
    --ink:#3f3f3f;
    --dark:#484848;
    --mid:#9a9a9a;
    --light:#d4d4d4;
    --faint:#ececec;
    --white:#ffffff;
  }
  *{box-sizing:border-box;margin:0;padding:0}
  html,body{width:1200px;height:859px;overflow:hidden;background:var(--bg)}
  body{position:relative;font-family:"Questrial",sans-serif;color:var(--ink)}
  .sheet{position:absolute;background:var(--paper);box-shadow:0 2px 6px rgba(0,0,0,.12);overflow:hidden}
  .lockup{font-family:"Cinzel",serif;font-weight:400;color:var(--ink);line-height:1.1}
  .lockup .name{display:block;letter-spacing:.12em;white-space:nowrap}
  .lockup .sub{display:block;letter-spacing:.08em;white-space:nowrap}
  .small{font-size:7px;line-height:1.45;color:var(--ink);white-space:nowrap}
  .band{position:absolute;left:0;width:100%}

  /* business card front */
  .card-front{left:40px;top:70px;width:240px;height:137px}
  .card-front .lockup{position:absolute;left:18px;top:18px}
  .card-front .name{font-size:17px}
  .card-front .sub{font-size:8px}
  .card-front .person{position:absolute;left:18px;top:72px;font-size:9px;letter-spacing:.05em}
  .card-front .contact{position:absolute;left:18px;top:96px}

  /* business card back */
  .card-back{left:40px;top:240px;width:240px;height:137px;background:var(--dark);color:var(--white)}
  .card-back .tag{position:absolute;left:18px;top:40px;border:1px solid var(--white);padding:4px 8px;font-family:"Cinzel",serif;font-size:9px;letter-spacing:.08em;color:var(--white)}
  .card-back .web{position:absolute;left:18px;top:78px;font-size:7px;color:var(--white)}

  /* letterhead */
  .letterhead{left:320px;top:36px;width:340px;height:481px}
  .letterhead .lockup{position:absolute;left:26px;top:26px}
  .letterhead .name{font-size:20px}
  .letterhead .sub{font-size:9px}
  .letterhead .contact{position:absolute;right:24px;top:30px;text-align:right}
  .letterhead .watermark{position:absolute;left:80px;top:150px}
  .letterhead .band{bottom:26px;height:12px}

  /* folder */
  .folder{left:700px;top:36px;width:460px;height:500px}
  .folder .lockup{position:absolute;right:40px;top:70px;text-align:right}
  .folder .name{font-size:30px}
  .folder .sub{font-size:13px}
  .folder .band{top:170px;height:330px}

  /* envelope front */
  .env-front{left:100px;top:590px;width:440px;height:210px}
  .env-front .lockup{position:absolute;left:24px;top:20px}
  .env-front .name{font-size:18px}
  .env-front .sub{font-size:8px}
  .env-front .contact{position:absolute;left:24px;top:64px}
  .env-front .band{bottom:22px;height:12px}

  /* envelope back */
  .env-back{left:620px;top:590px;width:440px;height:210px}
  .env-back .flap{position:absolute;left:0;top:0;width:100%;height:74px;background:var(--dark);display:flex;align-items:center;justify-content:center}
  .env-back .flap span{font-family:"Cinzel",serif;font-size:11px;letter-spacing:.14em;color:var(--white)}
</style>
</head>
<body>

  <section class="sheet card-front" aria-label="Business card front">
    <div class="lockup"><span class="name">HARBORLINE</span><span class="sub">VALET &amp; CONCIERGE</span></div>
    <p class="person">Elias R. Moreno</p>
    <div class="contact small">
      <p>Operations Manager</p>
      <p>Tel 705 555 0173</p>
      <p>Unit 48, 310 Tidewater Lane, Port Alder, ON</p>
    </div>
  </section>

  <section class="sheet card-back" aria-label="Business card back">
    <p class="tag">VALET &amp; CONCIERGE</p>
    <p class="web">www.harborlinevalet.com</p>
  </section>

  <section class="sheet letterhead" aria-label="Letterhead">
    <div class="lockup"><span class="name">HARBORLINE</span><span class="sub">VALET &amp; CONCIERGE</span></div>
    <div class="contact small">
      <p>Unit 48, 310 Tidewater Lane</p>
      <p>Port Alder, ON K9X 4P2</p>
      <p>Tel 705 555 0173</p>
      <p>info@harborlinevalet.com</p>
      <p>www.harborlinevalet.com</p>
    </div>
    <svg class="watermark" width="180" height="180" viewBox="0 0 180 180" role="img" aria-label="Faint valet watermark">
      <circle cx="90" cy="90" r="88" fill="var(--faint)"/>
    </svg>
    <svg class="band" viewBox="0 0 340 12" preserveAspectRatio="none" aria-hidden="true">
      <rect x="0" y="2" width="340" height="8" fill="var(--light)"/>
      <polygon points="0,0 118,0 126,12 0,12" fill="var(--dark)"/>
      <polygon points="126,2 340,2 340,10 131,10" fill="var(--mid)"/>
    </svg>
  </section>

  <section class="sheet folder" aria-label="Presentation folder">
    <div class="lockup"><span class="name">HARBORLINE</span><span class="sub">VALET &amp; CONCIERGE</span></div>
    <svg class="band" viewBox="0 0 460 330" preserveAspectRatio="none" aria-hidden="true">
      <polygon points="0,0 40,0 52,12 0,12" fill="var(--dark)"/>
      <polygon points="52,4 460,4 460,12 58,12" fill="var(--mid)"/>
      <polygon points="0,14 280,14 296,30 460,30 460,330 0,330" fill="var(--dark)"/>
      <polygon points="280,14 460,14 460,26 292,26" fill="var(--mid)"/>
    </svg>
  </section>

  <section class="sheet env-front" aria-label="Envelope front">
    <div class="lockup"><span class="name">HARBORLINE</span><span class="sub">VALET &amp; CONCIERGE</span></div>
    <div class="contact small">
      <p>Unit 48, 310 Tidewater Lane</p>
      <p>Port Alder, ON K9X 4P2</p>
    </div>
    <svg class="band" viewBox="0 0 440 12" preserveAspectRatio="none" aria-hidden="true">
      <rect x="0" y="2" width="440" height="8" fill="var(--light)"/>
      <polygon points="0,0 150,0 158,12 0,12" fill="var(--dark)"/>
      <polygon points="158,2 440,2 440,10 163,10" fill="var(--mid)"/>
    </svg>
  </section>

  <section class="sheet env-back" aria-label="Envelope back">
    <div class="flap"><span>VALET &amp; CONCIERGE</span></div>
  </section>

</body>
</html>
```